Calvanta Group Real Estate Company business cards

New business card design, we are generally happy with the basic layout of the existing front of business card, (feel free to change) but require a head shot photo on the back side.

http://www.calvanta.com.au/

Attached logos, and existing business card

------------------------------

Target Market(s)

Real estate

Industry/Entity Type

Real Estate

Contact Information for Business Card

Standard size double sided

Font styles to use
Other font styles liked:
• Futura

Requirements
Must have
• Photo head shot on the back side
Nice to have
• yes
Should not have
• No

```html
<!DOCTYPE html>
<html lang="en">
<head>
<meta charset="utf-8">
<title>Calvanta Group business cards</title>
<link href="https://fonts.googleapis.com/css2?family=Jost:wght@400;500&display=swap" rel="stylesheet">
<style>
  :root {
    --purple: #2e1f63;
    --orange: #f39325;
    --white: #ffffff;
    --ink: #1c1c1c;
    --grey: #6d6d6d;
    --stage: #ebe8e3;
  }
  * { margin: 0; padding: 0; box-sizing: border-box; }
  html, body {
    width: 1200px; height: 892px; overflow: hidden;
    background: var(--stage);
    font-family: "Jost", "Futura", sans-serif;
  }
  .sheet {
    width: 1200px; height: 892px;
    display: flex; align-items: center; justify-content: center; gap: 50px;
  }
  .card {
    position: relative;
    width: 525px; height: 300px;
    overflow: hidden;
    box-shadow: 0 6px 18px rgba(0,0,0,0.18);
  }
  .card svg.art { position: absolute; inset: 0; }
  .card-front { background: var(--white); }
  .card-back { background: var(--purple); }

  .brand-name {
    position: absolute;
    font-weight: 500;
    letter-spacing: -0.5px;
    line-height: 1;
    white-space: nowrap;
  }
  .card-front .brand-name { left: 40px; top: 58px; font-size: 46px; color: var(--purple); }
  .card-back .brand-name { left: 120px; top: 122px; font-size: 46px; color: var(--orange); }

  .person { position: absolute; left: 40px; top: 160px; }
  .person-name { font-size: 24px; color: var(--orange); font-weight: 400; line-height: 1.1; }
  .person-role { font-size: 15px; color: var(--ink); margin-top: 2px; }

  .divider {
    position: absolute; left: 228px; top: 150px;
    width: 1px; height: 60px; background: var(--ink);
  }
  .contacts {
    position: absolute; left: 244px; top: 150px;
    list-style: none; font-size: 13.5px; color: var(--ink);
  }
  .contacts li { display: flex; align-items: center; gap: 8px; height: 20px; }
  .contact-icon {
    width: 11px; height: 11px; background: var(--orange);
    display: flex; align-items: center; justify-content: center;
  }
  .contact-icon svg { width: 8px; height: 8px; }
</style>
</head>
<body>
<main class="sheet">

  <section class="card card-front" aria-label="Business card front">
    <svg class="art" viewBox="0 0 525 300" width="525" height="300" aria-hidden="false">
      <path class="swoosh-orange" d="M130,300 C290,282 430,222 525,158 L525,168 C432,232 300,290 170,300 Z" fill="var(--orange)"/>
      <path class="band-purple" d="M185,300 C320,288 440,236 525,180 L525,300 Z" fill="var(--purple)"/>
      <text class="abn" x="0" y="0" transform="translate(330 286) rotate(-17)" font-family="Jost, sans-serif" font-size="12.5" fill="var(--white)">ABN: 51 204 638 917</text>
    </svg>

    <div class="brand-name">calvanta group</div>

    <div class="person">
      <div class="person-name">Daniel Tran</div>
      <div class="person-role">Director</div>
    </div>

    <div class="divider"></div>

    <ul class="contacts">
      <li>
        <span class="contact-icon"><svg viewBox="0 0 8 8"><rect x="2" y="0.5" width="4" height="7" rx="0.8" fill="none" stroke="#fff" stroke-width="1"/></svg></span>
        0400 318 265
      </li>
      <li>
        <span class="contact-icon"><svg viewBox="0 0 8 8"><circle cx="4" cy="4" r="3" fill="none" stroke="#fff" stroke-width="1"/><line x1="1" y1="4" x2="7" y2="4" stroke="#fff" stroke-width="0.8"/></svg></span>
        www.calvanta.com.au
      </li>
      <li>
        <span class="contact-icon"><svg viewBox="0 0 8 8"><rect x="0.8" y="1.8" width="6.4" height="4.4" fill="none" stroke="#fff" stroke-width="0.9"/><polyline points="0.8,1.8 4,4.6 7.2,1.8" fill="none" stroke="#fff" stroke-width="0.9"/></svg></span>
        daniel.tran@calvanta.com.au
      </li>
    </ul>
  </section>

  <section class="card card-back" aria-label="Business card back">
    <svg class="art" viewBox="0 0 525 300" width="525" height="300">
      <defs>
        <linearGradient id="keyTone" x1="0" y1="0" x2="1" y2="1">
          <stop offset="0" stop-color="#d9d6e0"/>
          <stop offset="1" stop-color="#8c87a0"/>
        </linearGradient>
        <linearGradient id="portraitTone" x1="0" y1="0" x2="1" y2="1">
          <stop offset="0" stop-color="#e6e6e8"/>
          <stop offset="1" stop-color="#b8b9c0"/>
        </linearGradient>
      </defs>
      <path role="img" aria-label="Photo of a key in a door lock" d="M0,0 L210,0 C195,55 150,95 0,120 Z" fill="url(#keyTone)"/>
      <path role="img" aria-label="Head shot photo of the director" d="M525,300 L300,300 C318,235 332,190 380,160 L525,150 Z" fill="url(#portraitTone)"/>
    </svg>
    <div class="brand-name">calvanta group</div>
  </section>

</main>
</body>
</html>
```